New Business Card

We need to refresh our business cards. We designed these ourselves and we have no graphic design experience. We would like to find a new business card design that is professional and unique. We are an auto finance company. Feel free to play with the logo, but we would like to keep the eye very present on the card. Our corporate colors are green, grey, and white.
Green - RGB - 168,215,27; HEX - #AADD22
Grey - RGB - 196,196,196; HEX - #C4C4C4
Updates
Need to upload the vector file to finalize the project. The last logo was for a jpeg that didn't stretch well.
Industry/Entity Type
Financial Service
Contact Information for Business Card
Honestly don't know...I need your help!

```html
<!DOCTYPE html>
<html lang="en">
<head>
<meta charset="utf-8">
<title>Brightlane Capital – Business Card</title>
<link rel="stylesheet" href="https://fonts.googleapis.com/css2?family=Montserrat:wght@500;600;700&display=swap">
<style>
  :root {
    --brand-green: #aadd22;
    --text-green: #9cc42a;
    --brand-grey: #c4c4c4;
    --label-grey: #a9a9a9;
    --ink: #4a4a4c;
    --rule: #5a5a5c;
    --paper: #f4f4f2;
    --backdrop: #e6e8e3;
  }
  * { box-sizing: border-box; margin: 0; padding: 0; }
  html, body { width: 1200px; height: 800px; overflow: hidden; }
  body {
    background: var(--backdrop);
    font-family: "Montserrat", sans-serif;
    display: flex;
    align-items: center;
    justify-content: center;
    gap: 40px;
  }
  .card {
    width: 540px;
    height: 309px;
    background: var(--paper);
    position: relative;
    box-shadow: 0 2px 10px rgba(0,0,0,0.08);
  }

  /* Brand name block (used on both sides) */
  .brand { text-align: center; }
  .brand__row { display: inline-flex; align-items: center; gap: 10px; }
  .brand__dot {
    width: 16px; height: 16px; border-radius: 50%;
    background: var(--brand-green);
  }
  .brand__name {
    color: var(--text-green);
    font-weight: 600;
    letter-spacing: -0.5px;
  }
  .brand__sub {
    color: var(--label-grey);
    font-weight: 500;
    letter-spacing: 0.55em;
    margin-top: 6px;
    padding-left: 0.55em;
  }

  /* Back side */
  .card--back {
    display: flex; flex-direction: column;
    align-items: center; justify-content: center;
  }
  .card--back .brand__name { font-size: 46px; }
  .card--back .brand__sub { font-size: 16px; }
  .back-tags {
    position: absolute; bottom: 30px; left: 0; right: 0;
    display: flex; justify-content: center; align-items: center; gap: 18px;
    color: var(--text-green); font-size: 10px; font-weight: 600; letter-spacing: 0.08em;
  }
  .back-tags__dot { width: 7px; height: 7px; border-radius: 50%; background: var(--brand-green); }

  /* Front side */
  .card--front { display: flex; }
  .front-brand {
    width: 255px;
    display: flex; align-items: center; justify-content: center;
  }
  .card--front .brand__name { font-size: 30px; }
  .card--front .brand__sub { font-size: 11px; }
  .divider {
    position: absolute; left: 255px; top: 40px;
    width: 3px; height: 229px;
    background: linear-gradient(var(--rule) 0 35%, var(--brand-green) 35% 65%, var(--rule) 65% 100%);
  }
  .contact {
    padding: 48px 0 0 36px;
    color: var(--ink);
  }
  .contact__name { font-size: 17px; font-weight: 700; }
  .contact__name-first { color: var(--text-green); }
  .contact__title {
    display: inline-block; margin-top: 4px;
    background: var(--brand-green); color: #fff;
    font-size: 10px; font-weight: 600; padding: 2px 4px;
  }
  .contact__address { margin-top: 38px; font-size: 11.5px; font-weight: 600; line-height: 1.55; }
  .contact__lines { margin-top: 26px; font-size: 12px; font-weight: 600; line-height: 1.75; }
  .contact__phone { color: var(--text-green); }
</style>
</head>
<body>
  <section class="card card--back" aria-label="Card back">
    <div class="brand">
      <div class="brand__row"><span class="brand__dot"></span><span class="brand__name">Brightlane</span></div>
      <div class="brand__sub">CAPITAL</div>
    </div>
    <div class="back-tags"><span>AUTO LOANS</span><span class="back-tags__dot"></span><span>OFFER INFO</span></div>
  </section>

  <section class="card card--front" aria-label="Card front">
    <div class="front-brand">
      <div class="brand">
        <div class="brand__row"><span class="brand__dot"></span><span class="brand__name">Brightlane</span></div>
        <div class="brand__sub">CAPITAL</div>
      </div>
    </div>
    <div class="divider"></div>
    <div class="contact">
      <p class="contact__name"><span class="contact__name-first">Daniel</span> Okoro Price</p>
      <p class="contact__title">Creative Designer</p>
      <p class="contact__address">48 Alder Row, Kingsfield,<br>London N4 2QT, UK</p>
      <p class="contact__lines">
        <span class="contact__phone">+0000 2222 1234</span><br>
        mail@domain.com<br>
        www.website.com
      </p>
    </div>
  </section>
</body>
</html>
```